Qorvel Consulting

We focus on Data Recovery but we also do Network Security. We recover data from all types of hard drive form factors 3.5", 2.5", 1", 1.8", 5.25", 8" with any kind of interface IDE(PATA), SATA, mSATA, SCSI, SAS and Fibre Channel. All RAID Arrays 0, 1, 2, 3, 4, 5, 10 including nested levels like RAID 0+1, 1+0, 100, 0+3, 50 and 60, flash drives, like tablets, cellphones, usb drives, memory cards(SD, miniSD, Data Wafer(tavik))

Actually you can gather any information or text from any data recovery site, cause is usually the same info, we would probably change a couple of things from the description so it wont look the same. One thing though, we want to make clear to users not to attempt data recovery themselves and to ship the faulty device to us, maybe we can illustrate this?

the Data Recovery link can have sub menus like "Data Recovery Process - Data Recovery Services - F.A.Q"

the Penetration Testing can have sub menus like "F.A.Q - Pentest Process - Pentest Services"

Here are links from website so you gather information:

-http://www.mydiskwentdark.example/

-http://www.bitrescuelabsrecovery.example/

-http://www.pulvenbytes.example/

http://fetchlostfiles.example/lp/hard-drive-recovery.aspx?src=Brovix&gclid=ZTRWq4XplnQMDA-kwPbcf7HE2s
http://www.qulm.example/
http://www.venbrisfield.example/data-recovery/
http://www.tzwdatarecovery.example/

thanks.

Target Market(s)

Any PC user

Industry/Entity Type

Data Recovery

Requirements
Must have
• - Language and geographic navigation
- Home page navigation
- Global navigation
- Breadcrumbs
Nice to have
• - Sliders
-Drop down navigation

```html
<!DOCTYPE html>
<html lang="en">
<head>
<meta charset="utf-8">
<title>Qorvel Consulting – Data Recovery</title>
<link rel="stylesheet" href="https://fonts.googleapis.com/css2?family=Signika:wght@300;400;600&family=Open+Sans:wght@400;600&display=swap">
<style>
:root{
  --red:#d90d0d;
  --red-dark:#a80808;
  --red-deep:#8e0606;
  --ink:#222;
  --text:#7a7a7a;
  --dark:#2b2b2b;
  --darker:#1c1c1c;
  --light:#f2f2f2;
  --link:#1a8fd8;
  --white:#fff;
}
*{box-sizing:border-box;margin:0;padding:0}
html,body{width:1108px;height:1200px;overflow:hidden}
body{position:relative;background:var(--white);font-family:"Open Sans",Arial,sans-serif;color:var(--ink)}
a{color:inherit;text-decoration:none}

.locale-bar{position:absolute;top:0;left:0;width:1108px;height:20px;background:linear-gradient(#3a3a3a,#232323);color:#fff;font:600 11px "Open Sans",sans-serif;display:flex;justify-content:flex-end;align-items:center;padding-right:34px;gap:14px}
.locale-bar .lang{text-decoration:underline}
.locale-bar .caret{display:inline-block;border:4px solid transparent;border-top:5px solid #fff;margin-left:6px;vertical-align:-2px}

.site-header{position:absolute;top:20px;left:0;width:1108px;height:103px}
.brand{position:absolute;left:123px;top:34px;font:600 30px "Signika",sans-serif;color:var(--ink);display:flex;align-items:center;gap:10px}
.brand .mark{width:14px;height:14px;background:var(--red)}
.contact{position:absolute;right:122px;top:26px;text-align:right;font-family:"Signika",sans-serif}
.contact svg{position:absolute;left:-38px;top:2px}
.contact .label{color:var(--red);font-size:21px;font-weight:400}
.contact .label b{font-weight:600}
.contact .phone{color:#555;font-size:20px;font-weight:300;letter-spacing:1px;margin-top:2px}

.main-nav{position:absolute;top:123px;left:0;width:1108px;height:43px;background:linear-gradient(#e01414,#b80a0a);font:600 14px "Signika",sans-serif;color:#fff}
.main-nav a{position:absolute;top:0;height:43px;line-height:43px}
.main-nav .active{background:var(--dark);padding:0 0 0 29px;width:168px}
.main-nav .drop::after{content:"";display:inline-block;border:5px solid transparent;border-top:6px solid #fff;margin-left:12px;vertical-align:-2px}
.search-box{position:absolute;left:809px;top:8px;width:189px;height:27px;background:#fff;border-radius:3px;font:400 11px "Open Sans",sans-serif;color:#aaa;padding:6px 13px}
.search-box svg{position:absolute;right:9px;top:5px}

.sub-nav{position:absolute;top:166px;left:0;width:1108px;height:36px;background:linear-gradient(#3b3b3b,#2a2a2a);color:#eee;font:400 13px "Open Sans",sans-serif}
.sub-nav a{position:absolute;top:0;line-height:36px}

.hero{position:absolute;top:202px;left:0;width:1108px;height:361px;overflow:hidden}
.hero-bg{position:absolute;inset:0;background:linear-gradient(100deg,#d8d2cc 0%,#ece9e6 40%,#c4c0bc 62%,#3a3f4a 72%,#2a2d34 85%,#b9b4ae 100%)}
.hero h1{position:absolute;left:126px;top:82px;font:600 48px "Signika",sans-serif;color:var(--red);letter-spacing:-.5px}
.hero p{position:absolute;left:128px;top:148px;font:300 28px/32px "Signika",sans-serif;color:#111}
.hero .btn{position:absolute;left:130px;top:235px;width:143px;height:37px;background:linear-gradient(#fff,#e6e6e6);border:1px solid #ccc;border-radius:3px;font:400 19px/35px "Signika",sans-serif;color:#333;text-align:center;box-shadow:0 1px 2px rgba(0,0,0,.2)}

.band{position:absolute;top:563px;left:0;width:1108px;height:125px;background:linear-gradient(#fff 0%,#fff 75%,#ececec 100%)}
.services{position:absolute;top:563px;left:102px;width:904px;height:134px;background:linear-gradient(#e31111,#b50808);border-radius:0 0 10px 10px;display:flex;box-shadow:0 2px 4px rgba(0,0,0,.25)}
.service{position:relative;flex:1;border-right:1px solid var(--red-deep);padding:13px 0 0 18px;color:#fff}
.service:last-child{border-right:0}
.service h3{font:400 19px "Signika",sans-serif}
.service p{font:600 11.5px/17px "Open Sans",sans-serif;width:115px;margin-top:6px}
.service .more{position:absolute;left:18px;top:98px;background:#fff;color:#444;border-radius:3px;font:400 11px/21px "Open Sans",sans-serif;padding:0 12px;box-shadow:0 1px 2px rgba(0,0,0,.3)}
.service .art{position:absolute;right:20px;top:42px;width:70px;height:78px;background:linear-gradient(#cfd3d8,#6d737b);border-radius:4px}

.welcome{position:absolute;left:114px;top:752px;width:548px}
.welcome h2,.news h2{font:300 25px "Signika",sans-serif;color:#222}
.welcome p{font-size:11.5px;line-height:18.5px;color:var(--text);margin-top:18px}
.welcome p:first-of-type{margin-top:20px}
.divider{position:absolute;left:685px;top:746px;width:1px;height:234px;background:#e3e3e3}
.news{position:absolute;left:711px;top:752px;width:290px}
.news article{margin-top:16px}
.news article + article{margin-top:14px}
.news h4{font:400 13px "Open Sans",sans-serif;color:var(--red)}
.news time{display:block;font-size:11px;color:#444;margin:4px 0 5px}
.news p{font-size:11.5px;line-height:18.5px;color:#999}
.news p a{color:var(--link)}
.rule-left{position:absolute;left:110px;top:1013px;width:552px;height:1px;background:#e6e6e6}
.rule-right{position:absolute;left:711px;top:1013px;width:287px;height:1px;background:#e6e6e6}

.footer-bg{position:absolute;top:1097px;left:0;width:1108px;height:103px;background:linear-gradient(#3a3a3a,#1e1e1e)}
.quick{position:absolute;top:1015px;left:102px;width:904px;height:135px;background:#fff;border-radius:0 0 8px 8px;box-shadow:0 0 4px rgba(0,0,0,.15)}
.quick h2{position:absolute;left:23px;top:6px;font:400 23px "Signika",sans-serif;color:#222}
.quick ul{list-style:none;position:absolute;left:26px;top:37px;right:20px;display:flex;justify-content:space-between}
.quick li{text-align:center;font:400 14px "Signika",sans-serif;color:#333}
.quick li svg{display:block;margin:8px auto 0}

.site-footer{position:absolute;top:1164px;left:113px;width:884px;display:flex;justify-content:space-between;color:#ddd;font:400 12px "Open Sans",sans-serif}
.site-footer nav a+a::before{content:"|";margin:0 9px}
</style>
</head>
<body>

<div class="locale-bar"><a class="lang" href="#">English</a><span>|</span><a href="#">United States<span class="caret"></span></a></div>

<header class="site-header">
  <a class="brand" href="#"><span class="mark"></span>Qorvel Consulting</a>
  <div class="contact">
    <svg width="30" height="40" viewBox="0 0 30 40"><path d="M6 2c-3 2-5 5-4 10 2 10 9 20 16 25 3 2 6 1 8-1l-5-7-4 2C13 27 9 19 9 14l4-2-3-9z" fill="#777"/></svg>
    <div class="label"><b>Contact Us</b> Today!</div>
    <div class="phone">555-014-2877</div>
  </div>
</header>

<nav class="main-nav">
  <a href="#" style="left:134px">Home</a>
  <a href="#" style="left:232px">About</a>
  <a href="#" class="active drop" style="left:301px">Penetration Test</a>
  <a href="#" class="drop" style="left:492px">Data Receovery</a>
  <a href="#" style="left:653px">Careers</a>
  <a href="#" style="left:744px">Search</a>
  <div class="search-box">Keyword
    <svg width="16" height="16" viewBox="0 0 16 16"><circle cx="9.5" cy="6.5" r="5" fill="none" stroke="#888" stroke-width="1.3"/><path d="M6 10l-4.5 4.5" stroke="#888" stroke-width="1.5"/></svg>
  </div>
</nav>

<nav class="sub-nav">
  <a href="#" style="left:135px">Data Recovery Process</a>
  <a href="#" style="left:312px">Data Recovery Services</a>
  <a href="#" style="left:493px">F.A.Q</a>
</nav>

<section class="hero">
  <div class="hero-bg" role="img" aria-label="Photo of a stressed businessman holding his head in front of a laptop in a blurred office"></div>
  <h1>Lost Important Data?</h1>
  <p>OK Relax... we can probably still save it!<br>100% data guarantee</p>
  <a class="btn" href="#">Read More</a>
</section>

<div class="band"></div>
<section class="services">
  <div class="service"><h3>HardDisk Recovery</h3><p>Le Lorem Ipsum est simplement du faux texte</p><a class="more" href="#">Read More</a><div class="art" role="img" aria-label="Open hard disk drive illustration"></div></div>
  <div class="service"><h3>Raid Recovery</h3><p>Le Lorem Ipsum est simplement du faux texte</p><a class="more" href="#">Read More</a><div class="art" role="img" aria-label="Stacked RAID server illustration"></div></div>
  <div class="service"><h3>Flash Drive Recovery</h3><p>Le Lorem Ipsum est simplement du faux texte</p><a class="more" href="#">Read More</a><div class="art" role="img" aria-label="USB flash drive illustration"></div></div>
  <div class="service"><h3>Network Securities</h3><p>Le Lorem Ipsum est simplement du faux texte</p><a class="more" href="#">Read More</a><div class="art" role="img" aria-label="Blue padlock on network connector illustration"></div></div>
</section>

<section class="welcome">
  <h2>Welcome to Qorvel Consulting</h2>
  <p>Lorem ipsum dolor sit amet, consectetuer adipiscing elit, sed diam nonummy nibh euismod tincidunt ut laoreet dolore magna aliquam erat volutpat. Ut wisi enim ad minim veniam, quis nostrud exerci tation ullamcorper suscipit lobortis nisl ut aliquip ex ea commodo consequat. Duis autem vel eum iriure dolor in hendrerit in vulputate velit esse molestie consequat.</p>
  <p>vel illum dolore eu feugiat nulla facilisis at vero eros et accumsan et iusto odio dignissim qui blandit praesent luptatum zzril delenit augue duis dolore te feugait nulla facilisi. Nam liber tempor cum soluta nobis eleifend option congue nihil imperdiet doming id quod mazim placerat facer possim assum.</p>
  <p>Typi non habent claritatem insitam; est usus legentis in iis qui facit eorum claritatem. Investigationes demonstraverunt lectores legere me lius quod ii legunt saepius.</p>
</section>
<div class="divider"></div>
<section class="news">
  <h2>Latest News</h2>
  <article><h4>Lorem ipsum dolor sit ametsfs, con-</h4><time>Novermber 01, 2012</time><p>Lorem ipsum dolor sit amet, consectetuer adipiscing elit, sed diam nonummy nibh euismod tincidunt. ut laoreet dolore. <a href="#">Read More</a></p></article>
  <article><h4>Lorem ipsum dolor sit ametsfs, con-</h4><time>Novermber 01, 2012</time><p>Lorem ipsum dolor sit amet, consectetuer adipiscing elit, sed diam nonummy nibh euismod tincidunt. ut laoreet dolore. <a href="#">Read More</a></p></article>
</section>
<div class="rule-left"></div><div class="rule-right"></div>

<div class="footer-bg"></div>
<section class="quick">
  <h2>Quick Links</h2>
  <ul>
    <li>Hard Drive<svg width="24" height="30" viewBox="0 0 24 30"><rect x="1" y="1" width="22" height="28" rx="3" fill="#aaa"/><circle cx="12" cy="15" r="7" fill="#eee"/><circle cx="12" cy="15" r="2" fill="#aaa"/></svg></li>
    <li>RAID<svg width="26" height="28" viewBox="0 0 26 28"><rect x="1" y="2" width="24" height="7" rx="1" fill="#aaa"/><rect x="1" y="11" width="24" height="7" rx="1" fill="#aaa"/><rect x="1" y="20" width="24" height="7" rx="1" fill="#aaa"/></svg></li>
    <li>Mobile Phones<svg width="20" height="32" viewBox="0 0 20 32"><rect x="1" y="1" width="18" height="30" rx="3" fill="#aaa"/><rect x="4" y="5" width="12" height="19" fill="#eee"/></svg></li>
    <li>MP3 Players<svg width="36" height="46" viewBox="0 0 36 46"><rect x="2" y="1" width="16" height="28" rx="2" fill="#aaa"/><circle cx="10" cy="20" r="4" fill="#eee"/><path d="M22 8c0 10-4 20 0 28s10 2 10-10" fill="none" stroke="#aaa" stroke-width="1.5"/></svg></li>
    <li>Digital Cameras<svg width="32" height="26" viewBox="0 0 32 26"><rect x="1" y="6" width="30" height="19" rx="2" fill="#aaa"/><rect x="10" y="2" width="12" height="6" fill="#aaa"/><circle cx="16" cy="15" r="6" fill="#eee"/><circle cx="16" cy="15" r="3" fill="#aaa"/></svg></li>
    <li>Tablets<svg width="26" height="34" viewBox="0 0 26 34"><rect x="1" y="1" width="24" height="32" rx="3" fill="#aaa"/><rect x="4" y="4" width="18" height="25" fill="#eee"/></svg></li>
    <li>Memory Cards<svg width="28" height="32" viewBox="0 0 28 32"><path d="M1 1h20l6 6v24H1z" fill="#aaa"/><rect x="5" y="4" width="3" height="8" fill="#eee"/><rect x="10" y="4" width="3" height="8" fill="#eee"/><rect x="15" y="4" width="3" height="8" fill="#eee"/><rect x="5" y="18" width="18" height="9" fill="#eee"/></svg></li>
  </ul>
</section>

<footer class="site-footer">
  <span>Copyright 2012 Website Name. All Rights Reserved.</span>
  <nav><a href="#">Home</a><a href="#">About</a><a href="#">Penetration Test</a><a href="#">Data Receovery</a><a href="#">Careers</a></nav>
</footer>

</body>
</html>
```